Designs for a fundrasining event a Brown Tie Beer and Wine event

We need a flyer, brochure, and tickets for entry for a brown tie event that will be a beer and wine pairing fundraising event to be held on May 9th from 6pm to 10pm at the Maplecrest Restaurant in Cedar Lake, Indiana, USA. There will be approximately 10 silent auction items and 5 or so sponsors that we will want to have the logos of the sponsors on what we can as well, attached are the logo for Open Hearth Foundation, IV NFP, which is the nonprofit hosting the event, there is also a logo for Dunmore Law, LLC which is one of the sponsors (this is so you have an idea of the other 4 or so that we would also want incorporated somehow). Please ask as many questions as you may have to clarify.

Industry/Entity Type

Event

Contact Information for Business Card

Open Hearth
Wendy P. Halvorsen
President/CEO
(555)384-9062
www.openhearthfdn.example.org

New Card:
Marcus J. Halvorsen
Director
(555)627-3148
www.openhearthfdn.example.org

New Card:
Norma T. Halvorsen
Director
www.openhearthfdn.example.org

New Card:
Gerald K. Halvorsen
Director
www.openhearthfdn.example.org

Font styles to use
Script

Requirements
Must have
• I want a clean card for all 4 individuals with the logo that was attached.

```html
<!DOCTYPE html>
<html lang="en">
<head>
<meta charset="utf-8">
<title>Wine and Beer Pairing – Fundraiser Flyer</title>
<link href="https://fonts.googleapis.com/css2?family=Cinzel:wght@400&family=Oswald:wght@200;300;400;700&family=Roboto+Condensed:ital,wght@0,400;1,400&family=Crimson+Text&display=swap" rel="stylesheet">
<style>
  :root{
    --stage:#5d626c;
    --paper-light:#f1e2bf;
    --paper-dark:#dcc598;
    --brown:#4f1a12;
    --gold:#a8843a;
    --gold-line:#e9cf78;
    --ink:#2a2a2a;
    --white:#ffffff;
  }
  *{margin:0;padding:0;box-sizing:border-box;}
  html,body{width:1200px;height:1000px;overflow:hidden;background:var(--stage);}
  .flyer{
    position:absolute;left:291px;top:22px;width:618px;height:955px;
    background:radial-gradient(ellipse at 40% 40%,var(--paper-light) 0%,var(--paper-dark) 100%);
    overflow:hidden;font-family:"Oswald",sans-serif;color:var(--brown);
  }
  .abs{position:absolute;}
  .kicker{
    left:30px;width:560px;top:40px;height:32px;
    border-top:1.5px solid var(--brown);border-bottom:1.5px solid var(--brown);
    font-family:"Cinzel",serif;font-size:25px;line-height:30px;text-align:center;letter-spacing:.5px;
  }
  .drinks-photo{
    left:318px;top:103px;width:300px;height:730px;
    background:
      radial-gradient(ellipse 40% 30% at 28% 25%,rgba(90,10,20,.9),transparent 70%),
      radial-gradient(ellipse 45% 55% at 75% 60%,rgba(240,170,30,.95),transparent 72%),
      radial-gradient(ellipse 40% 12% at 75% 20%,rgba(250,245,235,.95),transparent 75%);
  }
  .title{font-weight:700;line-height:1;letter-spacing:-1px;}
  .title-wine{left:32px;top:100px;font-size:104px;}
  .title-and{left:36px;top:180px;font-size:118px;font-weight:200;color:var(--gold);letter-spacing:-2px;}
  .title-beer{left:32px;top:284px;font-size:100px;}
  .title-pairing{left:32px;top:372px;font-size:112px;}
  .extras{left:46px;top:488px;font-family:"Roboto Condensed",sans-serif;font-style:italic;font-size:14.5px;color:var(--gold);}
  .date{left:36px;top:530px;font-weight:300;font-size:24px;color:var(--gold);}
  .date sup{font-size:11px;}
  .tickets{left:32px;top:580px;font-weight:700;font-size:46px;line-height:1;}
  .tickets sup{font-size:22px;vertical-align:18px;}
  .venue{left:36px;top:640px;font-weight:700;font-size:20px;}
  .address{left:36px;top:664px;font-weight:400;font-size:14.5px;color:var(--ink);}
  .host{left:38px;top:712px;display:flex;align-items:center;gap:14px;}
  .host-dot{width:70px;height:70px;border-radius:50%;background:var(--brown);}
  .host-name{font-weight:300;font-size:22px;letter-spacing:2px;color:var(--ink);}
  .web{left:36px;top:790px;font-weight:700;font-size:33px;line-height:1;}
  .contact{left:36px;top:832px;font-family:"Roboto Condensed",sans-serif;font-size:13px;color:var(--ink);}
  .sponsors{
    left:0;top:858px;width:618px;height:97px;background:var(--white);border-top:4px solid var(--gold-line);
  }
  .sponsors-label{left:34px;top:14px;font-family:"Roboto Condensed",sans-serif;font-size:12px;color:var(--ink);}
  .sponsor-row{left:30px;top:44px;width:570px;display:flex;align-items:center;justify-content:space-between;}
  .sponsor{display:flex;align-items:center;gap:8px;font-family:"Crimson Text",serif;font-size:18px;color:var(--ink);}
  .sponsor-mark{width:24px;height:24px;border-radius:50%;background:#3c8fc6;}
</style>
</head>
<body>
  <main class="flyer">
    <h2 class="abs kicker">COLON CANCER RESEARCH FUNDRAISER</h2>
    <div class="abs drinks-photo" role="img" aria-label="Photo of a glass of red wine beside a tall frothy glass of golden beer"></div>
    <h1>
      <span class="abs title title-wine">WINE</span>
      <span class="abs title title-and">and</span>
      <span class="abs title title-beer">BEER</span>
      <span class="abs title title-pairing">PAIRING</span>
    </h1>
    <p class="abs extras">with HEAVY HORS-D'OEUVRES &amp; SILENT AUCTION!</p>
    <p class="abs date">SATURDAY, MAY 9<sup>TH</sup> 2015 &nbsp;|&nbsp; 6PM-10PM</p>
    <p class="abs tickets"><sup>$</sup>100 TICKETS</p>
    <p class="abs venue">MAPLECREST RESTAURANT</p>
    <p class="abs address">4210 Harbor View Rd., Cedar Lake, IN 46303</p>
    <div class="abs host">
      <span class="host-dot"></span>
      <span class="host-name">OPEN HEARTH</span>
    </div>
    <p class="abs web">OpenHearthFdn.example.org</p>
    <p class="abs contact">Contact Wendy Halvorsen at (555) 384-9062 or Wendy@OpenHearthFdn.example.org</p>
    <footer class="abs sponsors">
      <p class="abs sponsors-label">Sponsored by</p>
      <div class="abs sponsor-row">
        <span class="sponsor">DUNMORE LAW, LLC</span>
        <span class="sponsor">Company Name</span>
        <span class="sponsor">Your Logo</span>
        <span class="sponsor"><span class="sponsor-mark"></span>generic company</span>
      </div>
    </footer>
  </main>
</body>
</html>
```